About the book: It is an A5 size book, small 40 pages miniguide
Book title: The pocket handbook of housing loans
Book subtitle: The quiet road to plenty
Author: Tod Brisbane
Back cover content: Please see attached word document "back page"
Colours: Our company logo should go at the back of the book. One colour we can't use is red. As this is a finance book the red colour is seen negatively. may be light green? you are the expert.
I think lots of white space will work well.
NOTE: please read the back cover notes to get an understanding of what the book is about. It educates readers about finance in property investing. It makes sense that image used combines 'property' and 'finance'. please read back page document attached.
NOTE: it is a small A5 , 40 page book . Its a miniguide rather than a book .
Updates

Project Deadline Extended
Reason: Dear designers, Thank you for submitting your work over the last few days. Unfortunately we haven't been able to get back to you regarding the final selection of design as the Author of the book has been away on leave with his family without reliable internet access. He is now back and will be giving feedback as we go. We apologise for the time extension. Unfortunately the site didn’t allow me to limit the extension for less than 5 days but we may not require that long. Thanks again. Lulu

Project Deadline Extended
Reason: We apologies we hadn't finalized a decision on this project due to the person from our end being away. We would like to finalise this design as soon as possible.

Target Market(s)

22 - 45 age group. Most fall between 30-40. Both male and female. couples , individuals etc ...

Industry/Entity Type

Finance

Font styles to use
Other font styles liked:
• sabon/Aeriel. Let me know if any other suggestions.

Requirements
Nice to have
• use green colour if possible but not essential.

```html
<!DOCTYPE html>
<html lang="en">
<head>
<meta charset="utf-8">
<title>The pocket handbook of housing loans — Tod Brisbane</title>
<link rel="stylesheet" href="https://fonts.googleapis.com/css2?family=Cinzel:wght@500&family=Fira+Sans+Extra+Condensed:wght@600&family=Source+Sans+3:wght@600;700&family=Arimo:wght@400&display=swap">
<style>
  :root {
    --band-light: #abeb9c;
    --band-dark: #3f9a30;
    --ink-blue: #2c4b9b;
    --ink-green: #3c9a2b;
    --paper: #ffffff;
    --art-dark: #4a4a4a;
    --art-light: #dcdcdc;
    --art-accent: #7fdc6a;
  }
  * { margin: 0; padding: 0; box-sizing: border-box; }
  html, body { width: 1200px; height: 850px; overflow: hidden; background: var(--paper); }
  .cover-spread { position: relative; width: 1200px; height: 850px; background: var(--paper); overflow: hidden; }

  .band-top { position: absolute; left: 0; top: 0; width: 1200px; height: 92px; background: var(--band-light); }
  .band-bottom { position: absolute; left: 0; top: 726px; width: 1200px; height: 124px; background: var(--band-dark); }

  /* Back cover */
  .back-cover { position: absolute; left: 0; top: 0; width: 600px; height: 850px; }
  .back-heading { position: absolute; left: 0; width: 600px; top: 120px; text-align: center;
    font-family: "Source Sans 3", sans-serif; font-weight: 700; font-size: 18.5px; color: var(--ink-green); }
  .back-subheading { position: absolute; left: 0; width: 600px; top: 153px; text-align: center;
    font-family: "Source Sans 3", sans-serif; font-weight: 700; font-size: 20px; color: var(--ink-blue); }
  .back-copy { position: absolute; left: 56px; top: 194px; width: 500px;
    font-family: "Source Sans 3", sans-serif; font-weight: 600; font-size: 12.6px; line-height: 19px; color: var(--ink-blue); }
  .back-copy p { margin-bottom: 19px; }
  .back-copy ul { list-style: none; }
  .back-copy li { position: relative; padding-left: 11px; }
  .back-copy li::before { content: "•"; position: absolute; left: 0; color: var(--ink-green); }
  .back-copy li.gap { margin-top: 19px; }

  .publisher { position: absolute; left: 195px; top: 640px; }
  .publisher-name { display: flex; align-items: center; gap: 8px;
    font-family: "Source Sans 3", sans-serif; font-weight: 700; font-size: 21px; color: var(--ink-blue); }
  .publisher-mark { width: 14px; height: 14px; background: var(--ink-blue); }
  .publisher-tagline { margin-top: 4px; font-family: "Source Sans 3", sans-serif; font-weight: 600;
    font-size: 11.5px; color: var(--ink-blue); }

  /* Front cover */
  .author { position: absolute; left: 600px; width: 600px; top: 30px; padding-left: 145px;
    font-family: "Cinzel", serif; font-weight: 500; font-size: 29px; letter-spacing: 2px; color: var(--paper); }
  .cover-art { position: absolute; left: 632px; top: 92px; width: 524px; height: 450px; }
  .subtitle { position: absolute; right: 95px; top: 548px;
    font-family: "Arimo", Arial, sans-serif; font-size: 26px; color: var(--ink-blue); letter-spacing: 0.3px; }
  .subtitle-reflection { position: absolute; right: 95px; top: 572px; transform: scaleY(-1);
    font-family: "Arimo", Arial, sans-serif; font-size: 26px; color: var(--ink-blue); opacity: 0.12;
    -webkit-mask-image: linear-gradient(to top, #000 0%, transparent 60%); mask-image: linear-gradient(to top, #000 0%, transparent 60%); }
  .title { position: absolute; right: 58px; text-align: right;
    font-family: "Fira Sans Extra Condensed", sans-serif; font-weight: 600; line-height: 1; white-space: nowrap; }
  .title-line-1 { top: 664px; font-size: 60px; color: var(--ink-blue); }
  .title-line-2 { top: 734px; font-size: 62px; color: var(--paper); }
</style>
</head>
<body>
<div class="cover-spread">
  <div class="band-top"></div>
  <div class="band-bottom"></div>

  <section class="back-cover">
    <h2 class="back-heading">THE POCKET HANDBOOK OF HOUSING LOANS.</h2>
    <h3 class="back-subheading">The quiet road to plenty.</h3>
    <div class="back-copy">
      <p>The number-one reason most investors never own more than one property is finance.<br>
      For them, getting and managing money is the scariest part of investing.<br>
      You must be 100% informed when structuring your loans. Before you even think about finding a property, you must understand the valuation process.</p>
      <p>In simple, jargon-free language, this mini guide arms you with a wealth of knowledge to reduce risk and keep control of your investment goals.<br>
      Its many vital lessons include:</p>
      <ul>
        <li>How to keep your own home safe and out of the bank’s hands.</li>
        <li>The first step to successful investing is knowing where you want to finish. Learn how different exit strategies affect your investment plan.</li>
        <li class="gap">The main reason most Australians aren’t wealthy is that they don’t know the difference between appreciating and depreciating assets and beneficial and non-beneficial liabilities. Learn to view everything as one or the other.</li>
        <li class="gap">Grasping the concept of leverage and other people’s money will dramatically increase your return on equity.</li>
        <li class="gap">Banking and finance. By knowing what lenders need to asses a loan, you can apply with confidence and put yourself ahead of the pack.</li>
      </ul>
    </div>
    <div class="publisher">
      <div class="publisher-name"><span class="publisher-mark"></span>Greenvale Property Group</div>
      <div class="publisher-tagline">Wealth Building Through Property Investment</div>
    </div>
  </section>

  <section class="front-cover">
    <div class="author">TOD BRISBANE</div>
    <svg class="cover-art" viewBox="0 0 524 450" role="img" aria-label="Illustration of grey arrows splitting off to both sides while one green arrow runs straight down the middle">
      <defs>
        <linearGradient id="art-side" x1="0" y1="0" x2="0" y2="1">
          <stop offset="0" stop-color="var(--paper)"/>
          <stop offset="0.5" stop-color="var(--art-light)"/>
          <stop offset="1" stop-color="var(--paper)"/>
        </linearGradient>
        <linearGradient id="art-centre" x1="0" y1="0" x2="0" y2="1">
          <stop offset="0" stop-color="var(--art-dark)" stop-opacity="0.35"/>
          <stop offset="1" stop-color="var(--art-accent)" stop-opacity="0.5"/>
        </linearGradient>
      </defs>
      <rect width="524" height="450" fill="url(#art-side)"/>
      <rect x="202" width="120" height="450" fill="url(#art-centre)"/>
    </svg>
    <div class="subtitle">THE QUIET ROAD TO PLENTY</div>
    <div class="subtitle-reflection" aria-hidden="true">THE QUIET ROAD TO PLENTY</div>
    <h1>
      <span class="title title-line-1">THE POCKET HANDBOOK</span>
      <span class="title title-line-2">OF HOUSING LOANS</span>
    </h1>
  </section>
</div>
</body>
</html>
```